Lanterne architecture business cards

We are a new company based in New Zealand. We Specialize in High end Luxury Residential Architecture.

Every home is bespoke and is designed to each clients individual requirements and needs.

I like to design buildings that inspire people through light and form while offering a high level of comfort and usability.

Lines of sight, proportion and balance are fundamental to the spaces I create.
Updates

August 5th is current deadline - Today's date is the 13th of August.

Target Market(s)

New Zealanders who want a custom individual home design, typically 30-65 year old males and females

Industry/Entity Type

Architecture

Contact Information for Business Card

Director - Derek Tolson
Contact Number - 0279164073
Email - info@lanternearchitecture-example.co.nz
Webstie - www.lanternearchitecture-example.co.nz
Social Media - @lanternearchitecture

Font styles to use
Sans Serif

Requirements
Must have
• Logo (Both Sides)
Website
Email
Contact Number
Social Media

Nice to have
• Texture
Should not have
• More than 3 colours - typically I would've thought 2 would be good to match the logo.

```html
<!DOCTYPE html>
<html lang="en">
<head>
<meta charset="utf-8">
<title>Lanterne architecture business cards</title>
<link href="https://fonts.googleapis.com/css2?family=Raleway:wght@300;400&display=swap" rel="stylesheet">
<style>
  :root {
    --backdrop: #1a1a1a;
    --card-white: #ffffff;
    --card-black: #151515;
    --emboss-light: #2a2a2a;
    --ink: #111111;
    --ink-soft: #3a3a3a;
    --foil: #e6e6e6;
  }
  * { margin: 0; padding: 0; box-sizing: border-box; }
  html, body {
    width: 1200px; height: 711px; overflow: hidden;
    background: var(--backdrop);
    font-family: "Raleway", sans-serif;
  }
  .canvas {
    position: relative; width: 1200px; height: 711px;
    display: flex; align-items: center; justify-content: center; gap: 50px;
  }
  .card {
    position: relative; width: 525px; height: 300px; overflow: hidden;
  }
  .card--front { background: var(--card-white); color: var(--ink); }
  .card--back { background: var(--card-black); color: var(--foil); }

  .wordmark { position: absolute; text-align: center; }
  .wordmark__mark {
    display: block; width: 26px; height: 26px; margin: 0 auto 12px;
    border: 2px solid currentColor; border-radius: 50%;
  }
  .wordmark__name {
    display: block; font-weight: 400; font-size: 17px;
    letter-spacing: 0.62em; margin-right: -0.62em;
  }
  .wordmark__sub {
    display: block; font-weight: 300; font-size: 6.5px;
    letter-spacing: 0.95em; margin-right: -0.95em; margin-top: 5px;
  }
  .card--front .wordmark { top: 52px; right: 48px; color: var(--ink); }

  .social {
    position: absolute; right: 22px; bottom: 22px;
    display: flex; align-items: center; gap: 6px;
    font-size: 8.5px; font-weight: 400; letter-spacing: 0.02em; text-transform: uppercase;
  }
  .social__dot { width: 8px; height: 8px; background: var(--ink); }

  .contact { position: absolute; left: 30px; bottom: 26px; }
  .contact__name {
    font-weight: 300; font-size: 21px; letter-spacing: 0.04em;
    text-transform: uppercase; margin-bottom: 8px;
  }
  .contact__list { list-style: none; }
  .contact__item {
    display: flex; align-items: center; gap: 7px;
    font-size: 9.5px; font-weight: 400; letter-spacing: 0.03em;
    text-transform: uppercase; line-height: 15px; color: var(--ink-soft);
  }
  .contact__icon { width: 9px; height: 9px; flex: none; }

  .texture {
    position: absolute; inset: 0;
    background: radial-gradient(ellipse at 40% 45%, var(--emboss-light) 0%, var(--card-black) 75%);
  }
  .card--back .wordmark {
    top: 50%; left: 50%; transform: translate(-50%, -50%);
  }
  .card--back .wordmark__name { font-size: 22px; }
  .card--back .wordmark__sub { font-size: 8px; }
</style>
</head>
<body>
<main class="canvas">
  <section class="card card--front" aria-label="Card front">
    <div class="wordmark">
      <span class="wordmark__mark"></span>
      <span class="wordmark__name">LANTERNE</span>
      <span class="wordmark__sub">ARCHITECTURE</span>
    </div>
    <div class="social"><span class="social__dot"></span>@lanternearchitecture</div>
    <div class="contact">
      <p class="contact__name">Derek Tolson</p>
      <ul class="contact__list">
        <li class="contact__item">
          <svg class="contact__icon" viewBox="0 0 10 10"><path d="M2 0.5 L3.6 2.6 L2.8 3.6 Q4 6 6.4 7.2 L7.4 6.4 L9.5 8 L8.4 9.5 Q3.5 9 0.5 1.6 Z" fill="currentColor"/></svg>
          0279164073
        </li>
        <li class="contact__item">
          <svg class="contact__icon" viewBox="0 0 10 10"><rect x="0.5" y="2" width="9" height="6.5" fill="currentColor"/><path d="M0.8 2.3 L5 5.6 L9.2 2.3" stroke="#fff" stroke-width="0.8" fill="none"/></svg>
          info@lanternearchitecture-example.co.nz
        </li>
        <li class="contact__item">
          <svg class="contact__icon" viewBox="0 0 10 10"><circle cx="5" cy="5" r="4.3" fill="none" stroke="currentColor" stroke-width="1"/><ellipse cx="5" cy="5" rx="1.8" ry="4.3" fill="none" stroke="currentColor" stroke-width="0.8"/><line x1="0.7" y1="5" x2="9.3" y2="5" stroke="currentColor" stroke-width="0.8"/></svg>
          www.lanternearchitecture-example.co.nz
        </li>
      </ul>
    </div>
  </section>

  <section class="card card--back" aria-label="Card back">
    <div class="texture" role="img" aria-label="Blind-embossed repeating pattern on black stock"></div>
    <div class="wordmark">
      <span class="wordmark__name">LANTERNE</span>
      <span class="wordmark__sub">ARCHITECTURE</span>
    </div>
  </section>
</main>
</body>
</html>
```